Wordpress Theme for a Professional Speaker's Website

I I need a website to promote myself as a speaker to corporations and meeting planners. Some examples of similar sites I like are:

http://www.beginwithpurpose-demo.net (this is by far my favorite)
http://www.lorapemberton.net
http://www.teddyvance.net
http://www.bolsinter.net
http://www.dawnacrossridges.net
http://www.rudyfallenbrook.net

I like modern, minimalistic, innovative. I'm okay if it's edgy but still want it communicate professionalism.

The primary objective is to position me as an expert who can deliver valuable information in an entertaining manner.

There are two calls to action. The first is to capture name and email address to subscribe to my newsletter. The second is to request more information about booking me to speak for their company, organization, etc.

The pages on the website will ultimately be the following:

1. Home (should include sections for recent blog posts, featured topics/presentations, short bio, testimonials, email capture, and anything else you think should be added.
2. Meet Owen
3. Blog
4. Keynotes & Speaking
5. Training & Webinars
6. Coaching & Consulting
7. Testimonials
8. Book Owen
9. Media Inquiries
10. Contact

Please feel free to use your creativity. I don't want my requirements to limit you in any way. I'm just looking for a modern, professional site that will make me stand out from the crowd.

I don't have any existing site or brand identity. My plan is to have the website design I ultimately choose serve as the foundation for the rest of my brand identity.

Target Market(s)

Corporate meeting planners and executives

Industry/Entity Type

It Professional

Font styles to use
Sans Serif

Requirements
Must have
• Email capture, testimonials, blog
Nice to have
• None
Should not have
• None

```html
<!DOCTYPE html>
<html lang="en">
<head>
<meta charset="utf-8">
<title>Owen Castrell — Speaker</title>
<link rel="stylesheet" href="https://fonts.googleapis.com/css2?family=Open+Sans:ital,wght@0,400;0,600;0,700;0,800;1,400;1,600&display=swap">
<style>
:root{
  --orange:#ee6a2d;
  --blue:#5aa7bd;
  --blue-dark:#3f8fa6;
  --ink:#3a3a3a;
  --muted:#666;
  --light:#f1f1f1;
  --line:#dcdcdc;
  --dark:#2f2f2f;
  --darker:#262626;
  --white:#fff;
}
*{box-sizing:border-box;margin:0;padding:0}
html,body{width:1200px;height:3147px;overflow:hidden}
body{font-family:'Open Sans',Arial,sans-serif;color:var(--ink);background:var(--white);position:relative}
.sec{position:absolute;left:0;width:1200px}
.ph{display:block}

/* brand name */
.brand{position:absolute;left:161px;display:flex;align-items:center;gap:8px;font-weight:700;font-size:20px;line-height:20px;letter-spacing:.5px;white-space:nowrap;text-transform:uppercase}
.brand .mark{width:14px;height:14px;background:var(--orange)}
.header .brand{top:44px;color:var(--ink)}
.footer .brand{top:34px;color:var(--white)}

/* header */
.header{top:0;height:132px;background:var(--white);border-bottom:3px solid var(--blue)}
.topbar{position:absolute;right:0;top:0;height:46px;width:660px;background:var(--orange);clip-path:polygon(20px 0,100% 0,100% 100%,0 100%);display:flex;justify-content:flex-end;align-items:center;gap:36px;padding-right:86px;font-size:13px;font-weight:600;color:var(--white);text-transform:uppercase}
.mainnav{position:absolute;left:388px;top:83px;display:flex;gap:34px;font-size:13px;font-weight:600;text-transform:uppercase;color:var(--ink)}
.mainnav .on{color:var(--orange)}
.navtick{position:absolute;left:396px;top:116px;width:0;height:0;border:8px solid transparent;border-bottom-color:var(--blue)}

/* hero */
.hero{top:135px;height:541px;background:linear-gradient(#f7f7f7,#ececec)}
.hero-person{position:absolute;left:210px;top:20px;width:335px;height:521px;background:linear-gradient(#6a6a6a,#4a4a4a 60%,#3c3c3c);border-radius:140px 140px 0 0}
.hero h1{position:absolute;left:585px;top:180px;font-weight:800;line-height:1}
.hero h1 .l1{display:block;color:var(--orange);font-size:50px}
.hero h1 .l2{display:block;color:var(--blue);font-size:84px;margin-top:12px}
.dots{position:absolute;left:980px;top:462px;display:flex;gap:4px}
.dots i{width:12px;height:12px;border-radius:50%;background:#555}
.dots i.on{background:var(--orange)}

/* subscribe */
.subscribe{top:676px;height:92px;background:var(--orange)}
.subscribe .blueside{position:absolute;left:0;top:0;height:92px;width:485px;background:var(--blue);clip-path:polygon(0 0,100% 0,calc(100% - 26px) 100%,0 100%)}
.subscribe p{position:absolute;left:161px;top:22px;width:320px;color:var(--white);font-weight:700;font-size:15px;line-height:24px;text-transform:uppercase}
.field{position:absolute;background:var(--white);font-size:12px;font-style:italic;color:#555;padding:12px}
.btn{position:absolute;background:var(--orange);color:var(--white);font-size:13px;font-weight:700;text-transform:uppercase;display:flex;align-items:center;justify-content:center}
.subscribe .btn{background:var(--blue);left:929px;top:27px;width:107px;height:40px}

/* as seen */
.seen{top:768px;height:80px;background:var(--light);display:flex;align-items:center;justify-content:center;gap:30px}
.seen span{font-size:13px;font-weight:600;color:#555}
.badge{width:50px;height:22px;background:#9a9a9a;border-radius:3px}

h2.title{position:absolute;left:0;width:1200px;text-align:center;font-size:24px;font-weight:700;color:#4a4a4a;text-transform:uppercase}

/* featured */
.featured{top:848px;height:612px}
.featured h2{top:36px}
.topic{position:absolute;width:242px}
.topic .ph{height:145px;background:linear-gradient(135deg,#8a5a3a,#3a2a24)}
.topic h3,.post h3{color:var(--orange);font-size:14px;font-weight:700;margin-top:12px}
.topic p,.post p{font-size:11px;line-height:17px;color:#555;margin-top:6px}
.feature{position:absolute;left:705px;top:100px;width:331px}
.feature .ph{height:204px;background:linear-gradient(135deg,#3a2a2a,#111)}
.feature .meta{color:var(--orange);font-size:12px;font-weight:600;margin-top:18px}
.feature h3{color:var(--blue);font-size:17px;font-weight:700;line-height:24px;margin-top:10px}
.feature p{font-size:13px;line-height:22px;color:#555;margin-top:12px}
.feature .btn{position:static;width:110px;height:40px;margin-top:16px}
.play{position:absolute;width:44px;height:44px;border:2px solid rgba(255,255,255,.85);border-radius:50%}

/* about */
.about{top:1460px;height:449px;background:var(--light)}
.about h2{position:absolute;left:161px;top:62px;font-size:26px;font-weight:700;color:#4a4a4a;text-transform:uppercase}
.about .lead{position:absolute;left:161px;top:120px;width:580px;font-size:14px;line-height:22px;color:#555}
.about .body{position:absolute;left:161px;top:186px;width:560px;font-size:11px;line-height:19px;color:#555}
.about .btn{left:161px;top:330px;width:103px;height:38px}
.trailer{position:absolute;left:275px;top:330px;width:172px;height:38px;border:2px solid var(--blue);color:var(--blue);font-size:12px;font-weight:700;display:flex;align-items:center;justify-content:center;gap:8px;text-transform:uppercase}
.share{position:absolute;top:339px;width:22px;height:22px;background:#c9c9c9}
.mail{position:absolute;left:560px;top:324px}
.about-person{position:absolute;left:760px;top:10px;width:330px;height:439px;background:linear-gradient(#e4ddd2,#a59a88 55%,#7e715f);border-radius:160px 160px 0 0}

/* testimonials */
.testi{top:1909px;height:361px;background:linear-gradient(rgba(40,40,40,.92),rgba(40,40,40,.92)),linear-gradient(90deg,#555,#333,#555)}
.testi h2{top:62px;color:var(--white)}
.arrows{position:absolute;left:986px;top:66px;display:flex;gap:6px}
.arrows i{width:24px;height:24px;border:2px solid #ddd;border-radius:50%;display:flex;align-items:center;justify-content:center;color:#ddd;font-style:normal;font-size:12px}
.arrows i.off{opacity:.4}
.avatar{position:absolute;left:190px;top:135px;width:124px;height:124px;border-radius:50%;border:5px solid var(--white);background:linear-gradient(#e7c39a,#b5835a)}
.quote{position:absolute;left:340px;top:130px;width:672px;color:#e4e4e4;font-style:italic;font-size:13px;line-height:24px}
.quote b{color:var(--white);font-size:22px;font-style:normal;font-weight:800}
.cite{position:absolute;left:342px;top:220px;color:var(--white);font-size:13px;font-weight:700}
.cite small{font-size:11px;font-weight:600;color:#ccc}

/* blog */
.blog{top:2270px;height:401px}
.blog h2{top:22px}
.post{position:absolute;top:84px;width:204px}
.post .ph{height:139px;background:linear-gradient(135deg,#b9a58a,#4a5a78)}
.post .pmeta{display:flex;gap:24px;font-size:11px;font-weight:600;color:#444;margin-top:16px}

/* booking */
.booking{top:2671px;height:245px;background:var(--blue)}
.booking h2{top:24px;color:var(--white)}
.booking .field{height:36px;padding:10px;font-size:11px}
.booking .btn{left:527px;top:178px;width:146px;height:38px}

/* footer */
.footer{top:2916px;height:231px;background:var(--dark)}
.fnav{position:absolute;left:409px;top:32px;width:640px;display:flex;flex-wrap:wrap;column-gap:16px;row-gap:14px;font-size:11.5px;font-weight:600;color:var(--white);text-transform:uppercase}
.frule{position:absolute;left:161px;right:164px;top:106px;border-top:1px solid #444}
.keep{position:absolute;left:161px;top:124px;font-size:10px;font-weight:600;color:#bbb;text-transform:uppercase}
.social{position:absolute;left:161px;top:150px;display:flex;gap:4px}
.social i{width:30px;height:30px;border-radius:50%;background:var(--blue);border:2px solid var(--white)}
.footer .field{top:136px;height:40px}
.footer .btn{left:891px;top:136px;width:145px;height:40px}
.copy{position:absolute;right:164px;top:200px;font-size:11px;color:#ddd}
</style>
</head>
<body>

<header class="sec header">
  <nav class="topbar"><span>Blog</span><span>Testimonials</span><span>Book Owen</span><span>Media Inquiries</span><span>Contact</span></nav>
  <div class="brand"><i class="mark"></i>Owen Castrell</div>
  <nav class="mainnav"><span class="on">Home</span><span>Meet Owen</span><span>Keynotes &amp; Speaking</span><span>Training &amp; Webinars</span><span>Coaching &amp; Consulting</span></nav>
  <span class="navtick"></span>
</header>

<section class="sec hero">
  <div class="hero-person" role="img" aria-label="Photo of the speaker in a grey suit gesturing on stage"></div>
  <h1><span class="l1">BUILD A BETTER</span><span class="l2">BUSINESS</span></h1>
  <div class="dots"><i></i><i></i><i class="on"></i><i></i></div>
</section>

<section class="sec subscribe">
  <div class="blueside"></div>
  <p>Subscribe an email address get your business secrets</p>
  <div class="field" style="left:487px;top:27px;width:212px;height:40px">Name:</div>
  <div class="field" style="left:707px;top:27px;width:212px;height:40px">Email address</div>
  <div class="btn">Subscribe</div>
</section>

<section class="sec seen">
  <span>AS SEEN ON :</span>
  <i class="badge"></i><i class="badge"></i><i class="badge"></i><i class="badge"></i><i class="badge"></i><i class="badge"></i>
</section>

<section class="sec featured">
  <h2 class="title">Featured Topics/Presentations</h2>
  <article class="topic" style="left:161px;top:100px">
    <div class="ph" role="img" aria-label="Photo of a speaker addressing a large audience"></div>
    <h3>Finibus Bonorum</h3><p>At vero eos et accusamus et iusto odio dignissi mo s ducimus qui blanditiis praesentium.</p>
  </article>
  <article class="topic" style="left:428px;top:100px">
    <div class="ph" role="img" aria-label="Photo of a seated conference audience"></div>
    <h3>Finibus Bonorum</h3><p>At vero eos et accusamus et iusto odio dignissi mo s ducimus qui blanditiis praesentium.</p>
  </article>
  <article class="topic" style="left:161px;top:339px">
    <div class="ph" role="img" aria-label="Photo of business people in a meeting" style="background:linear-gradient(135deg,#c8ccd4,#3c4658)"></div>
    <h3>Finibus Bonorum</h3><p>At vero eos et accusamus et iusto odio dignissi mo s ducimus qui blanditiis praesentium.</p>
  </article>
  <article class="topic" style="left:428px;top:339px">
    <div class="ph" role="img" aria-label="Photo of a trainer presenting at a whiteboard" style="background:linear-gradient(135deg,#e6e2da,#8a7a6a)"></div>
    <h3>Finibus Bonorum</h3><p>At vero eos et accusamus et iusto odio dignissi mo s ducimus qui blanditiis praesentium.</p>
  </article>
  <article class="feature">
    <div class="ph" role="img" aria-label="Video still of the speaker presenting on a dark stage"></div>
    <span class="play" style="left:143px;top:78px"></span>
    <div class="meta">11:59 | March 2014</div>
    <h3>Sed ut ploremerspiciloatis unde omn nat ed ut perspiciatis un.</h3>
    <p>Sed ut perspiciatis unde omnis istenatus er or sit voluptatem accusantium doloremque laudantium, totam rem aperiam, eaue ipsa quae ab illo inventore veritatis et quasi.</p>
    <div class="btn">Read More</div>
  </article>
</section>

<section class="sec about">
  <h2>About Owen Castrell</h2>
  <p class="lead">Sed ut perspiciatis unde omnis iste natus error sit voluptatem accusantium doloremque laudantium, totam rem aperiam, eaque ipsa quae ab one voluptatem.</p>
  <p class="body">Sed ut perspiciatis unde omnis iste natus error sit voluptatem accusantium doloremque laudantium, totam rem aperiam, eaque ipsa quae ab illo inventore veritatis et quasi architecto beatae vitae dicta sunt explicabo. Nemo enim ipsam voluptatem quia voluptas sit aspernatur aut odit aut fugit, sed quia consequuntur magni dolores eos qui ratione voluptatem sequi nesciunt. Neque porro quisquam est, qui dolorem ipsumenim ipsam voluptatem quia voluptas sit aspernatur aut odit aut fugit, sed quia consequuntur magni dolores eos qui ratione voluptatem sequi nesciunt. Neque porro quisquam est, qui dolorem ipsu.</p>
  <div class="btn">Read More</div>
  <div class="trailer"><svg width="12" height="12" viewBox="0 0 12 12"><path d="M2 1l9 5-9 5z" fill="#5aa7bd"/></svg>Watch the Trailer</div>
  <i class="share" style="left:462px"></i><i class="share" style="left:487px"></i><i class="share" style="left:512px"></i>
  <svg class="mail" width="60" height="50" viewBox="0 0 60 50"><path d="M4 20L30 2l26 18v28H4z" fill="#e6e6e6" stroke="#888" stroke-width="2"/><rect x="14" y="10" width="32" height="22" fill="#fff" stroke="#ccc"/><path d="M4 20l26 18 26-18" fill="none" stroke="#888" stroke-width="2"/><path d="M14 14h32v6H14z" fill="#ee6a2d"/></svg>
  <div class="about-person" role="img" aria-label="Portrait of the speaker in a tweed jacket"></div>
</section>

<section class="sec testi">
  <h2 class="title">Testimonials</h2>
  <div class="arrows"><i>&#8249;</i><i class="off">&#8250;</i></div>
  <div class="avatar" role="img" aria-label="Portrait of a client"></div>
  <p class="quote"><b>&ldquo;</b> Sed ut perspiciatis unde omnis iste natus error sit voluptatem accusantium doloremque laudantium, totam rem aperiam, eaque ipsa quae ab illo inventore veritatis et quasi architecto beatae vitae dicta sunt explicaboni mpsam voluptatem quia voluptas sit aspernatur aut odit aut fugit, sed quia consequuntur magni <b>&rdquo;</b></p>
  <div class="cite">JHON SMITH, <small>CITY NAME, LOREM SIPMDIL</small></div>
</section>

<section class="sec blog">
  <h2 class="title">Recent Blog Posts</h2>
  <article class="post" style="left:161px"><div class="ph" role="img" aria-label="Photo of a presenter in a training room"></div><h3>Finibus Bonorum</h3><p>Sed ut perspiciatis unde omnis ite nats error sit voluptatemelod ut perspiciatis un domnis ite natus ervoluptatem.</p><div class="pmeta"><span>&#9633; Aug 05,2016</span><span>&#9679; Comments</span></div></article>
  <article class="post" style="left:386px"><div class="ph" role="img" aria-label="Photo of a speaker in front of a projection screen" style="background:linear-gradient(135deg,#e8ecf0,#2a3a5a)"></div><h3>Finibus Bonorum</h3><p>Sed ut perspiciatis unde omnis ite nats error sit voluptatemelod ut perspiciatis un domnis ite natus ervoluptatem.</p><div class="pmeta"><span>&#9633; Aug 05,2016</span><span>&#9679; Comments</span></div></article>
  <article class="post" style="left:608px"><div class="ph" role="img" aria-label="Photo of an applauding audience" style="background:linear-gradient(135deg,#d8b070,#3a4a7a)"></div><h3>Finibus Bonorum</h3><p>Sed ut perspiciatis unde omnis ite nats error sit voluptatemelod ut perspiciatis un domnis ite natus ervoluptatem.</p><div class="pmeta"><span>&#9633; Aug 05,2016</span><span>&#9679; Comments</span></div></article>
  <article class="post" style="left:833px"><div class="ph" role="img" aria-label="Photo of a workshop at a flip chart" style="background:linear-gradient(135deg,#eef0ec,#5a6a5a)"></div><h3>Finibus Bonorum</h3><p>Sed ut perspiciatis unde omnis ite nats error sit voluptatemelod ut perspiciatis un domnis ite natus ervoluptatem.</p><div class="pmeta"><span>&#9633; Aug 05,2016</span><span>&#9679; Comments</span></div></article>
</section>

<section class="sec booking">
  <h2 class="title">Booking Form</h2>
  <div class="field" style="left:161px;top:84px;width:210px">Name:</div>
  <div class="field" style="left:377px;top:84px;width:210px">Phone:</div>
  <div class="field" style="left:593px;top:84px;width:204px">Date:<svg style="position:absolute;right:10px;top:11px" width="12" height="12" viewBox="0 0 12 12"><rect x="1" y="2" width="10" height="9" fill="none" stroke="#444" stroke-width="1.5"/><path d="M1 5h10" stroke="#444"/></svg></div>
  <div class="field" style="left:808px;top:84px;width:228px;height:78px">Description:</div>
  <div class="field" style="left:161px;top:126px;width:210px">Company:</div>
  <div class="field" style="left:377px;top:126px;width:210px">Email:</div>
  <div class="field" style="left:593px;top:126px;width:204px">Location:<svg style="position:absolute;right:10px;top:10px" width="10" height="14" viewBox="0 0 10 14"><path d="M5 13C1 8 1 6 1 5a4 4 0 018 0c0 1 0 3-4 8z" fill="#444"/></svg></div>
  <div class="btn">Booking Now</div>
</section>

<footer class="sec footer">
  <div class="brand"><i class="mark"></i>Owen Castrell</div>
  <nav class="fnav"><span>Home</span><span>Meet Owen</span><span>Blog</span><span>Keynotes &amp; Speaking</span><span>Training &amp; Webinars</span><span>Coaching &amp; Consulting</span><span>Testimonials</span><span>Book Owen</span><span>Media Inquiries</span><span>Contact</span></nav>
  <div class="frule"></div>
  <div class="keep">Keep in touch</div>
  <div class="social"><i></i><i></i><i></i><i style="background:var(--orange)"></i></div>
  <div class="field" style="left:409px;width:230px">Name:</div>
  <div class="field" style="left:650px;width:230px">Email:</div>
  <div class="btn">Subscribe Here</div>
  <div class="copy">&copy; 2016 Owen Castrell. All right reserved Term of Use</div>
</footer>

</body>
</html>
```